Harbor Nightclub

Nightclub flyer., digital single sided, for KV and PX. I included samples of some previous flyers we've used. Sample Info:
HARBOR
FRIDAYS
FRI MAY 1 2020
DJ VORTAN (club floor)
DJ RUZO & DJ TAV (residents on the lounge floor)
4217 Marlow Avenue Sacramento
www.harborvenuehall.example for list/VIP inquiries

Target Market(s)

Upscale top 40 crowd but want some cool and artsy like the examples included.

Font styles to use
Sans Serif

Requirements
Must have
• Harbor Logo
Nice to have
• Would be nice if the flyer can be incorporated later with DJ photos (sometimes we will add dj photos to pixagram etc). Would like a big city type of feel.
Should not have
• Nothing too sexual.

```html
<!DOCTYPE html>
<html lang="en">
<head>
<meta charset="utf-8">
<title>Harbor Fridays Flyer</title>
<link rel="stylesheet" href="https://fonts.googleapis.com/css2?family=Oswald:wght@400&family=Josefin+Sans:wght@400;700&family=Lato:wght@300;400;700&display=swap">
<style>
  :root {
    --canvas: #d9d9d7;
    --ink: #f2f2f4;
    --ink-soft: #d6d8e0;
    --night: #05050f;
    --deep-blue: #14165a;
    --violet: #6a2aa8;
    --glow-cyan: #4fc3e8;
    --frame-line: #7fd6e6;
    --rule: #8a94a8;
    --band-start: #3b4550;
    --band-end: #6e8e96;
    --band-url: #1f2a33;
    --band-text: #c9d6da;
  }
  * { margin: 0; padding: 0; box-sizing: border-box; }
  html, body { width: 1200px; height: 1200px; overflow: hidden; }
  body { background: var(--canvas); position: relative; }

  .flyer {
    position: absolute; left: 180px; top: 5px;
    width: 840px; height: 1190px; overflow: hidden;
    background: var(--night);
  }
  .flyer-photo {
    position: absolute; inset: 0;
    background:
      radial-gradient(circle at 8% 8%, rgba(150,90,210,.55), transparent 28%),
      radial-gradient(circle at 92% 52%, rgba(79,195,232,.45), transparent 14%),
      radial-gradient(circle at 85% 18%, rgba(79,195,232,.30), transparent 22%),
      radial-gradient(circle at 12% 58%, rgba(180,190,230,.25), transparent 13%),
      radial-gradient(circle at 40% 25%, rgba(70,60,200,.55), transparent 40%),
      linear-gradient(160deg, var(--violet) 0%, var(--deep-blue) 38%, #0b0b30 65%, var(--night) 100%);
  }
  .frame-lines { position: absolute; left: 0; top: 0; }

  .wordmark {
    position: absolute; left: 0; width: 100%; top: 255px;
    text-align: center; color: var(--ink);
  }
  .wordmark-dot {
    display: block; width: 60px; height: 60px; margin: 0 auto 14px;
    border-radius: 50%; background: var(--ink);
  }
  .wordmark-name {
    font-family: "Lato", sans-serif; font-weight: 300;
    font-size: 54px; letter-spacing: 0.02em; line-height: 1;
  }

  .headline {
    position: absolute; left: 0; width: 100%; top: 418px;
    text-align: center; color: var(--ink);
    font-family: "Oswald", sans-serif; font-weight: 400;
    font-size: 190px; line-height: 1; letter-spacing: 0.2em; padding-left: 0.2em;
  }

  .date {
    position: absolute; left: 55px; top: 828px;
    font-family: "Oswald", sans-serif; font-weight: 400;
    color: var(--ink); font-size: 68px; line-height: 82px; letter-spacing: 0.32em;
  }
  .divider {
    position: absolute; left: 300px; top: 822px;
    width: 2px; height: 202px; background: var(--rule);
  }
  .lineup { position: absolute; left: 345px; top: 828px; color: var(--ink); }
  .act { margin-bottom: 26px; }
  .act-name {
    font-family: "Josefin Sans", sans-serif; font-weight: 700;
    font-size: 52px; line-height: 1; letter-spacing: 0.02em;
  }
  .act-name .dj { font-size: 36px; }
  .act-name .plus { font-size: 30px; margin: 0 6px; }
  .act-floor {
    margin-top: 8px;
    font-family: "Lato", sans-serif; font-weight: 400;
    font-size: 16px; letter-spacing: 0.28em; color: var(--ink-soft);
  }

  .venue-line {
    position: absolute; left: 55px; top: 1060px; width: 730px;
    display: flex; align-items: center;
    font-family: "Lato", sans-serif; font-weight: 300;
    color: var(--ink); font-size: 24px; letter-spacing: 0.05em;
  }
  .venue-sep { margin: 0 36px 0 44px; }
  .venue-mark { display: flex; align-items: center; gap: 8px; font-size: 27px; }
  .venue-mark-dot { width: 28px; height: 28px; border-radius: 50%; background: var(--ink); }

  .info-band {
    position: absolute; left: 0; bottom: 0; width: 100%; height: 66px;
    background: linear-gradient(90deg, var(--band-start), var(--band-end) 70%, var(--band-start));
    display: flex; align-items: center; justify-content: center;
    font-family: "Lato", sans-serif; font-size: 23px; letter-spacing: 0.08em;
  }
  .info-url { font-weight: 700; color: var(--band-url); }
  .info-note { font-weight: 400; color: var(--band-text); margin-left: 8px; }
</style>
</head>
<body>
  <main class="flyer">
    <div class="flyer-photo" role="img" aria-label="Glowing jellyfish drifting through a starry purple and blue night sky"></div>

    <svg class="frame-lines" width="840" height="1190" viewBox="0 0 840 1190" aria-hidden="true">
      <g fill="none" stroke="var(--frame-line)" stroke-width="2" opacity="0.85">
        <polygon points="385,110 655,375 470,790 160,430"/>
        <polygon points="405,105 670,395 450,795 170,415"/>
        <polygon points="425,100 680,420 430,800 180,400"/>
        <polygon points="445,102 690,445 410,795 195,385"/>
      </g>
    </svg>

    <div class="wordmark">
      <span class="wordmark-dot"></span>
      <div class="wordmark-name">HARBOR</div>
    </div>

    <h1 class="headline">FRIDAY</h1>

    <div class="date">MAY/1<br>2020</div>
    <div class="divider"></div>

    <section class="lineup">
      <div class="act">
        <div class="act-name"><span class="dj">DJ</span> VORTAN</div>
        <div class="act-floor">CLUB FLOOR</div>
      </div>
      <div class="act">
        <div class="act-name"><span class="dj">DJ</span> RUZO<span class="plus">+</span><span class="dj">DJ</span> TAV</div>
        <div class="act-floor">RESIDENTS ON THE LOUNGE FLOOR</div>
      </div>
    </section>

    <div class="venue-line">
      <span class="venue-address">4217 MARLOW AVENUE, SACRAMENTO</span>
      <span class="venue-sep">|</span>
      <span class="venue-mark"><span class="venue-mark-dot"></span>HARBOR</span>
    </div>

    <footer class="info-band">
      <span class="info-url">www.harborvenuehall.example</span>
      <span class="info-note">for list/VIP inquiries</span>
    </footer>
  </main>
</body>
</html>
```